Packaging design for a reclosable bag for our product

We have a logo, and we need to put it on packaging for our product and while we want the look to be simple, we want it to follow good design principles and also contain spaces for other product descriptions.

There will be 5 sizes at launch so I'd like 5 variations, one for each size.

I've included a few mockups of the type of bag that I made but they are all just rough ideas that I had.

I want the brand to look scientific and methodical and even a bit quirky, as in "wow this is a serious product but also a bit unusual."

```html
<!DOCTYPE html>
<html lang="en">
<head>
<meta charset="utf-8">
<title>NV4 Bias Lighting – M Pouch</title>
<link href="https://fonts.googleapis.com/css2?family=Mulish:wght@400;800;900&display=swap" rel="stylesheet">
<style>
  :root {
    --page-bg: #ffffff;
    --pouch-black: #141414;
    --side-strip: #262626;
    --size-band: #0c0c0c;
    --zip-line: #0a0a0a;
    --accent-yellow: #f6c000;
    --text-white: #ffffff;
    --text-soft: #ececec;
  }
  html, body {
    margin: 0;
    padding: 0;
    width: 1200px;
    height: 1200px;
    overflow: hidden;
    background: var(--page-bg);
    font-family: "Mulish", "Helvetica Neue", Arial, sans-serif;
  }
  .canvas {
    position: relative;
    width: 1200px;
    height: 1200px;
  }
  .pouch {
    position: absolute;
    left: 272px;
    top: 100px;
    width: 657px;
    height: 1000px;
    background: var(--pouch-black);
    border-radius: 30px 30px 0 0;
    overflow: hidden;
  }
  .side-strip {
    position: absolute;
    left: 0;
    top: 0;
    width: 110px;
    height: 100%;
    background: var(--side-strip);
  }
  .zip-track {
    position: absolute;
    left: 0;
    width: 100%;
    height: 3px;
    background: var(--zip-line);
    opacity: 0.8;
  }
  .zip-track.one { top: 92px; }
  .zip-track.two { top: 112px; height: 5px; }
  .zip-track.three { top: 136px; }
  .size-band {
    position: absolute;
    left: 6px;
    top: 631px;
    width: 104px;
    height: 155px;
    background: var(--size-band);
  }
  .size-badge {
    position: absolute;
    left: 6px;
    top: 656px;
    width: 106px;
    height: 105px;
    background: var(--accent-yellow);
    color: var(--text-white);
    font-weight: 900;
    font-size: 50px;
    display: flex;
    align-items: center;
    justify-content: center;
  }
  .label {
    position: absolute;
    left: 136px;
    top: 548px;
    color: var(--text-white);
  }
  .brand-name {
    font-weight: 900;
    font-size: 104px;
    line-height: 84px;
    letter-spacing: -4px;
    margin: 0;
  }
  .product-name {
    font-weight: 800;
    font-size: 45px;
    line-height: 52px;
    margin: 18px 0 0;
  }
  .product-length {
    color: var(--accent-yellow);
    font-weight: 400;
    font-size: 28px;
    line-height: 36px;
    margin: 12px 0 0;
  }
  .product-spec {
    color: var(--text-soft);
    font-weight: 400;
    font-size: 28px;
    line-height: 38px;
    margin: 20px 0 0;
  }
</style>
</head>
<body>
  <main class="canvas">
    <section class="pouch">
      <div class="side-strip"></div>
      <div class="zip-track one"></div>
      <div class="zip-track two"></div>
      <div class="zip-track three"></div>
      <div class="size-band"></div>
      <div class="size-badge">M</div>
      <div class="label">
        <h1 class="brand-name">NV4</h1>
        <h2 class="product-name">Bias Lighting</h2>
        <p class="product-length">3 Meters / 9.8 Feet</p>
        <p class="product-spec">White Bias Lighting<br>6500K / Simulated D65 / CRI 90+</p>
      </div>
    </section>
  </main>
</body>
</html>
```